BrivoLane Ute.

I want the full logo on one side. And the other side the card if right Ralf the logo the left half orange like the car in the logo color with Danielle R Morrow
Founder and CEO
Email symbol then dmorrow@brivolaneute.com
Www symbol. Then Brivolaneute.com
Phone symbol then 413-926-BRIV
The very bottom would like Brivo Lane Ute is a division of Harmond Vistas. LLC

```html
<!DOCTYPE html>
<html lang="en">
<head>
<meta charset="utf-8">
<title>Brivo Lane Ute — Business Card</title>
<link href="https://fonts.googleapis.com/css2?family=Cinzel:wght@400;600&display=swap" rel="stylesheet">
<style>
  :root {
    --backdrop: #2a2a2a;
    --paper: #ececea;
    --ink: #1e1e1e;
    --orange: #e08a2a;
    --orange-deep: #d57a1f;
    --cream: #fbe9cc;
    --car-teal: #6fb7a8;
  }
  * { box-sizing: border-box; margin: 0; padding: 0; }
  html, body { width: 1200px; height: 764px; overflow: hidden; }
  body {
    background: var(--backdrop);
    font-family: "Cinzel", Georgia, serif;
    position: relative;
  }
  .card {
    position: absolute;
    top: 240px;
    width: 436px;
    height: 282px;
    background: var(--paper);
    box-shadow: 0 6px 14px rgba(0,0,0,0.45);
    overflow: hidden;
  }
  .card--front { left: 133px; }
  .card--back { left: 632px; }

  .logo-art {
    position: absolute;
    border-radius: 6px;
    background: linear-gradient(180deg, var(--car-teal) 0%, var(--orange) 45%, var(--orange-deep) 100%);
  }
  .logo-name {
    position: absolute;
    left: 0; right: 0;
    text-align: center;
    color: var(--ink);
    font-weight: 400;
    letter-spacing: 0.5px;
    white-space: nowrap;
  }
  .card--front .logo-art { left: 135px; top: 78px; width: 171px; height: 82px; }
  .card--front .logo-name { top: 163px; font-size: 30px; }

  .orange-field { position: absolute; left: 0; top: 0; width: 436px; height: 262px; }
  .card--back .logo-art { left: 282px; top: 112px; width: 104px; height: 42px; border-radius: 4px; }
  .card--back .logo-name { left: 246px; right: auto; width: 176px; top: 155px; font-size: 18px; }

  .holder {
    position: absolute;
    left: 22px; top: 64px;
    color: var(--cream);
  }
  .holder__name { font-size: 17px; font-weight: 400; letter-spacing: 0.3px; white-space: nowrap; }
  .holder__title { font-size: 10.5px; margin-top: 4px; padding-left: 33px; }

  .contacts {
    position: absolute;
    left: 18px; top: 141px;
    list-style: none;
    color: var(--cream);
    font-size: 9px;
    letter-spacing: 0;
  }
  .contacts li { display: flex; align-items: center; height: 21.5px; white-space: nowrap; }
  .contacts svg { width: 16px; height: 16px; margin-right: 8px; flex: none; }

  .division {
    position: absolute;
    left: 0; right: 0; bottom: 0;
    height: 20px;
    line-height: 22px;
    text-align: center;
    font-size: 8.5px;
    color: var(--ink);
    white-space: nowrap;
  }
</style>
</head>
<body>

<section class="card card--front" aria-label="Card front">
  <div class="logo-art" role="img" aria-label="Logo illustration: orange vintage wagon with surfboard and bottles between picket fences"></div>
  <div class="logo-name">Brivo Lane Ute</div>
</section>

<section class="card card--back" aria-label="Card back">
  <svg class="orange-field" viewBox="0 0 436 262" aria-hidden="true">
    <path d="M0 0 H208 C232 35 240 90 222 128 C210 152 212 205 238 262 H0 Z" fill="var(--orange)"/>
  </svg>

  <div class="holder">
    <p class="holder__name">Danielle R Morrow</p>
    <p class="holder__title">Founder and CEO</p>
  </div>

  <ul class="contacts">
    <li>
      <svg viewBox="0 0 16 16" aria-hidden="true"><rect x="1.5" y="3.5" width="13" height="9" fill="none" stroke="currentColor" stroke-width="1.2"/><path d="M1.5 3.5 L8 9 L14.5 3.5" fill="none" stroke="currentColor" stroke-width="1.2"/></svg>
      dmorrow@brivolaneute.com
    </li>
    <li>
      <svg viewBox="0 0 16 16" aria-hidden="true"><circle cx="8" cy="8" r="6.8" fill="none" stroke="currentColor" stroke-width="1.1"/><path d="M5.6 4.6 L6.8 4.4 L7.4 6.2 L6.6 7 C7 8 7.9 8.9 9 9.4 L9.8 8.6 L11.6 9.2 L11.4 10.4 C9 11 5 7 5.6 4.6 Z" fill="currentColor"/></svg>
      413-926-BRIV
    </li>
    <li>
      <svg viewBox="0 0 16 16" aria-hidden="true"><g fill="none" stroke="currentColor" stroke-width="1.1"><circle cx="8" cy="8" r="6.8"/><ellipse cx="8" cy="8" rx="3" ry="6.8"/><path d="M1.2 8 H14.8 M2.4 4.6 H13.6 M2.4 11.4 H13.6"/></g></svg>
      Brivolaneute.com
    </li>
  </ul>

  <div class="logo-art" role="img" aria-label="Logo illustration: orange vintage wagon with surfboard and bottles between picket fences"></div>
  <div class="logo-name">Brivo Lane Ute</div>

  <p class="division">Brivo Lane Ute is a division of Harmond Vistas. LLC</p>
</section>

</body>
</html>
```